Business Card Design

We are a new residential construction company.our team is made up of young highly skilled tradesman of the next generation of carpenters coming through with new skills and ideas.we chose the name meridian as it means strikingly different from the rest as this is what we plan to be and we would like to portray this in our business card.we like Bold lettering as we want to make a statement, also the use of colour would be great as we want to stand out from the usual plain construction cards and logos.
I have attached a logo sketch I did as a rough idea if you can tidy it up or improve on it would be good.
I have also attached the LBP logo please include this on the card small but still legible.
open to any colourschemes ideas.
thanks
(note)please delete the LBP#804317 off from the card details please.
Industry/Entity Type
Construction
Contact Information for Business Card
MERIDIAN CONSTRUCTION LIMITED
Director:Tom Halvick
Mobile :0217364820
Email:Meridian.Construction@quillpost.example
Address:48 Wendle place,Ashgrove park 2091,Auckland
LBP#BP804317

```html
<!DOCTYPE html>
<html lang="en">
<head>
<meta charset="utf-8">
<title>Meridian Construction – Business Card</title>
<link rel="stylesheet" href="https://fonts.googleapis.com/css2?family=Questrial&display=swap">
<style>
  :root {
    --red: #ec1c24;
    --sky: #00aeef;
    --blue: #0072bc;
    --yellow: #fff200;
    --green: #22b24c;
    --ink: #231f20;
    --white: #ffffff;
    --logo-blue: #1f5fb4;
    --black: #000000;
  }
  * { box-sizing: border-box; margin: 0; padding: 0; }
  html, body { width: 1200px; height: 900px; overflow: hidden; background: var(--white); }
  body { position: relative; font-family: "Questrial", sans-serif; }

  .card { position: absolute; overflow: hidden; background: var(--white); border: 1px solid #ddd; }

  /* Front */
  .card-front { left: 40px; top: 40px; width: 570px; height: 340px; }
  .card-front .block { position: absolute; }
  .front-red    { left: 0; top: 0; width: 70px; height: 205px; background: var(--red); }
  .front-sky    { left: 0; top: 210px; width: 70px; height: 130px; background: var(--sky); }
  .front-panel  { left: 75px; top: 0; width: 405px; height: 340px; background: var(--ink); }
  .front-yellow { left: 485px; top: 0; width: 85px; height: 140px; background: var(--yellow); }
  .front-green  { left: 485px; top: 145px; width: 85px; height: 195px; background: var(--green); }
  .front-wordmark { position: absolute; left: 75px; top: 0; width: 405px; height: 340px;
    display: flex; flex-direction: column; justify-content: center; align-items: flex-end;
    padding: 60px 40px 20px 0; color: var(--white); line-height: 1; }
  .front-wordmark .name { font-size: 78px; letter-spacing: -1px; }
  .front-wordmark .sub  { font-size: 38px; margin-top: 2px; }

  /* Back */
  .card-back { left: 25px; top: 445px; width: 590px; height: 370px; }
  .card-back .block { position: absolute; }
  .back-title { left: 0; top: 0; width: 415px; height: 215px; background: var(--sky);
    color: var(--white); font-size: 34px; line-height: 1.32; padding: 55px 0 0 18px; letter-spacing: .5px; }
  .back-badge { left: 420px; top: 0; width: 170px; height: 170px; background: var(--white);
    display: flex; align-items: center; justify-content: center; }
  .badge-shape { width: 116px; height: 116px; border-radius: 50%; background: var(--ink); }
  .back-director { left: 0; top: 220px; width: 205px; height: 150px; background: var(--yellow);
    color: var(--ink); padding: 20px 0 0 14px; }
  .avatar { width: 50px; height: 60px; border-radius: 25px 25px 8px 8px;
    background: linear-gradient(#4a8fe0, #12408f); margin-left: 40px; }
  .director-role { font-size: 22px; margin-top: 14px; }
  .director-name { font-size: 28px; font-weight: 700; }
  .back-phone { left: 210px; top: 220px; width: 120px; height: 90px; background: var(--red);
    color: var(--white); padding: 12px 0 0 10px; font-size: 16px; }
  .back-phone svg { display: block; margin-bottom: 10px; }
  .back-address { left: 335px; top: 175px; width: 255px; height: 135px; background: var(--blue);
    color: var(--white); display: flex; gap: 12px; padding: 14px 8px 0 12px; font-size: 16px; line-height: 1.4; }
  .back-email { left: 210px; top: 315px; width: 380px; height: 55px; background: var(--green);
    color: var(--white); display: flex; align-items: center; gap: 8px; padding-left: 12px; font-size: 13.5px; }

  /* Logo versions */
  .logo { position: absolute; left: 700px; width: 480px; height: 390px;
    display: flex; flex-direction: column; justify-content: center; align-items: flex-end;
    padding-right: 20px; line-height: 1; }
  .logo .name { font-size: 112px; letter-spacing: -2px; }
  .logo .sub  { font-size: 56px; margin-top: 4px; }
  .logo-blue  { top: 20px; color: var(--logo-blue); }
  .logo-black { top: 470px; color: var(--black); }
</style>
</head>
<body>

  <section class="card card-front" aria-label="Business card front">
    <div class="block front-red"></div>
    <div class="block front-sky"></div>
    <div class="block front-panel"></div>
    <div class="block front-yellow"></div>
    <div class="block front-green"></div>
    <div class="front-wordmark">
      <span class="name">meridian</span>
      <span class="sub">construction</span>
    </div>
  </section>

  <section class="card card-back" aria-label="Business card back">
    <div class="block back-title">MERIDIAN<br>CONSTRUCTION<br>LIMITED</div>
    <div class="block back-badge"><div class="badge-shape" role="img" aria-label="Licensed building practitioner badge"></div></div>
    <div class="block back-director">
      <div class="avatar" role="img" aria-label="Person icon"></div>
      <p class="director-role">Director:</p>
      <p class="director-name">Tom Halvick</p>
    </div>
    <div class="block back-phone">
      <svg width="20" height="24" viewBox="0 0 20 24" aria-hidden="true"><path d="M5 1 L8 6 L6 9 Q8 14 12 17 L15 15 L19 19 L16 23 Q4 20 1 5 Z" fill="#fff"/></svg>
      0217364820
    </div>
    <div class="block back-address">
      <svg width="48" height="72" viewBox="0 0 48 72" aria-hidden="true"><path d="M24 3 A21 21 0 0 1 45 24 Q45 38 24 69 Q3 38 3 24 A21 21 0 0 1 24 3 Z" fill="none" stroke="#fff" stroke-width="4"/><circle cx="24" cy="24" r="8" fill="#fff"/></svg>
      <p>48 Wendle place,<br>Ashgrove park 2091,<br>Auckland</p>
    </div>
    <div class="block back-email">
      <svg width="22" height="16" viewBox="0 0 22 16" aria-hidden="true"><rect x="1" y="1" width="20" height="14" fill="none" stroke="#fff" stroke-width="2"/><path d="M1 1 L11 9 L21 1" fill="none" stroke="#fff" stroke-width="2"/></svg>
      Meridian.Construction@quillpost.example
    </div>
  </section>

  <div class="logo logo-blue" aria-label="Meridian Construction logo, colour">
    <span class="name">meridian</span>
    <span class="sub">construction</span>
  </div>

  <div class="logo logo-black" aria-label="Meridian Construction logo, black">
    <span class="name">meridian</span>
    <span class="sub">construction</span>
  </div>

</body>
</html>
```